Business Card for Brevel Coatings

We need a simple, yet out standing business card for our painting company.

Target Market(s)

wealthy; high-end neighborhoods, and businesses

Industry/Entity Type

Painting

Contact Information for Business Card

Name:
Doran Vask

Email:
d.vask@brevel-coatings.com

Website:
Brevel-coatings.com

Phone Number:
(555) 416-9073

Font styles to use
Serif
Sans Serif

Requirements
Must have
• slogan "fresh walls made easy"
Should not have
• A title attached to the name on the card

```html
<!DOCTYPE html>
<html lang="en">
<head>
<meta charset="utf-8">
<title>Brevel Coatings – Business Card</title>
<link rel="stylesheet" href="https://fonts.googleapis.com/css2?family=Marcellus&family=Open+Sans:wght@300;400&family=Montserrat:wght@500&display=swap">
<style>
  :root {
    --forest: #3f5a22;
    --lime: #a6c22c;
    --card: #f4f4f2;
    --backdrop: #e4e5e1;
    --on-dark: #ffffff;
  }
  * { box-sizing: border-box; margin: 0; padding: 0; }
  html, body { width: 1200px; height: 800px; overflow: hidden; }
  body {
    background: var(--backdrop);
    position: relative;
    font-family: "Open Sans", Arial, sans-serif;
  }
  .card {
    position: absolute;
    width: 525px;
    height: 300px;
    background: var(--card);
    box-shadow: 0 6px 18px rgba(0,0,0,.12);
    overflow: hidden;
  }
  /* Front */
  .card--front { left: 100px; top: 90px; }
  .brand {
    display: flex;
    align-items: center;
    gap: 14px;
    color: var(--forest);
    font-family: "Marcellus", Georgia, serif;
    white-space: nowrap;
  }
  .brand__dot {
    flex: none;
    border-radius: 50%;
    background: var(--lime);
  }
  .card--front .brand {
    position: absolute;
    right: 42px;
    top: 92px;
    font-size: 46px;
  }
  .card--front .brand__dot { width: 40px; height: 40px; }
  .slogan {
    position: absolute;
    right: 42px;
    top: 172px;
    color: var(--lime);
    font-weight: 300;
    font-size: 27px;
    white-space: nowrap;
  }
  /* Back */
  .card--back { left: 575px; top: 410px; }
  .card--back .brand {
    position: absolute;
    left: 26px;
    top: 133px;
    font-size: 23px;
    gap: 8px;
  }
  .card--back .brand__dot { width: 20px; height: 20px; }
  .contact-panel {
    position: absolute;
    left: 246px;
    top: 22px;
    width: 250px;
    height: 278px;
    background: var(--forest);
    clip-path: polygon(0 0, 100% 0, 100% 80%, 78% 100%, 0 100%);
    color: var(--on-dark);
    padding: 34px 0 0 22px;
  }
  .contact-panel__name {
    font-family: "Montserrat", Arial, sans-serif;
    font-weight: 500;
    font-size: 18px;
    letter-spacing: 1px;
    text-transform: uppercase;
    margin-bottom: 22px;
  }
  .contact-list { list-style: none; }
  .contact-list li {
    display: flex;
    align-items: center;
    gap: 12px;
    font-size: 12.5px;
    margin-bottom: 16px;
    white-space: nowrap;
  }
  .contact-list svg { width: 28px; height: 28px; flex: none; }
</style>
</head>
<body>

  <section class="card card--front" aria-label="Business card front">
    <div class="brand"><span class="brand__dot"></span><span class="brand__name">Brevel Coatings</span></div>
    <p class="slogan">fresh walls made easy</p>
  </section>

  <section class="card card--back" aria-label="Business card back">
    <div class="brand"><span class="brand__dot"></span><span class="brand__name">Brevel Coatings</span></div>
    <div class="contact-panel">
      <h1 class="contact-panel__name">Doran Vask</h1>
      <ul class="contact-list">
        <li>
          <svg viewBox="0 0 28 28" aria-hidden="true" fill="none" stroke="#fff" stroke-width="1.3">
            <circle cx="14" cy="14" r="12.5"/>
            <path d="M10 8.5l2 0 1 3-1.5 1.2a7 7 0 0 0 3.8 3.8L16.5 15l3 1v2a1.5 1.5 0 0 1-1.6 1.5A10 10 0 0 1 8.5 10 1.5 1.5 0 0 1 10 8.5z" fill="#fff" stroke="none"/>
          </svg>
          <span>(555) 416-9073</span>
        </li>
        <li>
          <svg viewBox="0 0 28 28" aria-hidden="true" fill="none" stroke="#fff" stroke-width="1.3">
            <circle cx="14" cy="14" r="12.5"/>
            <circle cx="14" cy="14" r="6.5"/>
            <ellipse cx="14" cy="14" rx="3" ry="6.5"/>
            <path d="M7.5 14h13"/>
          </svg>
          <span>Brevel-coatings.com</span>
        </li>
        <li>
          <svg viewBox="0 0 28 28" aria-hidden="true" fill="none" stroke="#fff" stroke-width="1.3">
            <circle cx="14" cy="14" r="12.5"/>
            <rect x="8" y="10" width="12" height="8.5" fill="#fff" stroke="none"/>
            <path d="M8 10l6 5 6-5" stroke="#3f5a22"/>
          </svg>
          <span>d.vask@brevel-coatings.com</span>
        </li>
      </ul>
    </div>
  </section>

</body>
</html>
```